Income Tax Business Cards - Updates

Need to update these business cards while keeping all the same wording but just update them and make them look nicer and more modern/ on brand with our brand.

Industry/Entity Type

finance

Contact Information for Business Card

we have multiple locations so will just need to easily be able to change the address and phone numbers

Colors

Designer to choose colors to be used in the design.

```html
<!DOCTYPE html>
<html lang="en">
<head>
<meta charset="utf-8">
<title>Tax Advance Business Cards</title>
<link rel="stylesheet" href="https://fonts.googleapis.com/css2?family=Montserrat:wght@600;700;800&family=Tinos:wght@400;700&display=swap">
<style>
  :root {
    --green: #0f5230;
    --red: #b71c26;
    --white: #ffffff;
    --ink: #1d1d1d;
    --page: #e9e9e6;
  }
  * { box-sizing: border-box; margin: 0; padding: 0; }
  html, body { width: 1200px; height: 912px; overflow: hidden; }
  body {
    background: var(--page);
    font-family: "Montserrat", Arial, sans-serif;
    display: flex; flex-direction: column; align-items: center; justify-content: center; gap: 40px;
  }
  .card {
    position: relative; width: 700px; height: 400px; border-radius: 22px; overflow: hidden;
    box-shadow: 0 10px 28px rgba(0,0,0,.18);
  }
  .brand {
    display: flex; align-items: center; gap: 10px;
    font-family: "Tinos", "Times New Roman", serif; font-weight: 700;
  }
  .brand-dot { width: 14px; height: 14px; border-radius: 50%; flex: none; }

  /* Front */
  .card-front { background: var(--green); color: var(--white); text-align: center; }
  .card-front .brand { position: absolute; top: 38px; left: 0; right: 0; justify-content: center; font-size: 30px; color: var(--white); }
  .card-front .brand-dot { background: var(--white); }
  .tax-band {
    position: absolute; top: 118px; left: 0; right: 0; height: 64px; background: var(--red);
    font-family: "Tinos", "Times New Roman", serif; font-weight: 700; font-size: 44px;
    line-height: 64px; letter-spacing: 1px;
  }
  .front-amount { position: absolute; top: 200px; left: 0; right: 0; font-weight: 800; font-size: 86px; line-height: 1; }
  .front-advance { position: absolute; top: 300px; left: 0; right: 0; font-weight: 700; font-size: 36px; letter-spacing: 4px; }

  /* Back */
  .card-back { background: var(--white); }
  .back-shape { position: absolute; inset: 0; }
  .card-back .brand { position: absolute; top: 78px; left: 50px; font-size: 32px; line-height: 1.1; color: var(--green); }
  .card-back .brand-dot { background: var(--red); }
  .contact { position: absolute; left: 60px; top: 250px; color: var(--ink); }
  .contact-phone { font-weight: 700; font-size: 34px; margin-bottom: 10px; }
  .contact-address { font-family: Arial, sans-serif; font-size: 20px; line-height: 1.35; }
  .offer { position: absolute; left: 440px; top: 18px; width: 250px; text-align: center; color: var(--white); }
  .offer-upto { font-weight: 800; font-size: 34px; line-height: 1; }
  .offer-amount { font-weight: 800; font-size: 76px; line-height: 1; }
  .offer-advance, .offer-free {
    font-family: "Tinos", "Times New Roman", serif; font-weight: 700; color: var(--red);
    text-shadow: 1px 1px 0 var(--white), -1px -1px 0 var(--white), 1px -1px 0 var(--white), -1px 1px 0 var(--white);
  }
  .offer-advance { font-size: 30px; line-height: 1.1; margin-top: 6px; }
  .offer-note { font-family: Arial, sans-serif; font-size: 15px; margin-top: 2px; }
  .offer-free { font-size: 32px; line-height: 1; margin-top: 14px; }
</style>
</head>
<body>
  <section class="card card-front">
    <div class="brand"><span class="brand-dot"></span>Ledgerline Financial Group</div>
    <div class="tax-band">FILE YOUR TAXES HERE</div>
    <div class="front-amount">UP TO $6000</div>
    <div class="front-advance">SAME DAY ADVANCE</div>
  </section>

  <section class="card card-back">
    <svg class="back-shape" width="700" height="400" viewBox="0 0 700 400" aria-hidden="true">
      <path d="M330 0 Q350 330 700 370 L700 0 Z" fill="var(--green)"/>
      <path d="M315 0 Q332 348 700 385" fill="none" stroke="var(--red)" stroke-width="5"/>
    </svg>
    <div class="brand"><span class="brand-dot"></span><span>Ledgerline<br>Financial Group</span></div>
    <div class="contact">
      <div class="contact-phone">(555) 555-5555</div>
      <div class="contact-address">2710 Harbor Lane<br>Maple Grove, NY 11090</div>
    </div>
    <div class="offer">
      <div class="offer-upto">UP TO</div>
      <div class="offer-amount">$6000</div>
      <div class="offer-advance">Same day advance</div>
      <div class="offer-note">on approved tax returns!</div>
      <div class="offer-free">FREE<br>ESTIMATES!</div>
    </div>
  </section>
</body>
</html>
```